Property letting UK website

I need a web design for a new Property letting company in the UK. I already have a logo that was produced and won by a brief forge logo designer last week.

I like modern designs and require ease of functionality and usage. I already have a domain name registered so need to be able to link to that domain.

Regards,

Morven.

Target Market(s)

UK property

Industry/Entity Type

It Company

Number of Pages Required

5+ page

Requirements
Must have
• Home page, Current properties to let page, About us page, Contact us page, Testimonials page and ability to link to twitter and Facebook account.

```html
<!DOCTYPE html>
<html lang="en">
<head>
<meta charset="utf-8">
<title>Hearth Lets — Property Letting</title>
<link href="https://fonts.googleapis.com/css2?family=Tinos:wght@400&family=Oswald:wght@400&family=Arimo:wght@400&display=swap" rel="stylesheet">
<style>
:root{
  --header-bg:#333333;
  --logo-bg:#2a2a2a;
  --nav-bg:#262626;
  --nav-line:#3a3a3a;
  --accent:#0aa8e6;
  --page-bg:#f7f7f7;
  --rule:#d6d6d6;
  --title-grey:#9a9a9a;
  --heading:#333333;
  --white:#ffffff;
}
*{margin:0;padding:0;box-sizing:border-box}
html,body{width:1195px;height:1200px;overflow:hidden}
body{background:var(--page-bg);font-family:"Tinos",serif;position:relative}
.site-header{position:absolute;left:0;top:0;width:1195px;height:166px;
  background:repeating-linear-gradient(45deg,#353535 0 2px,#303030 2px 4px)}
.brand{position:absolute;left:126px;top:0;width:269px;height:135px;background:var(--logo-bg);
  display:flex;align-items:center;justify-content:center;gap:12px}
.brand-mark{width:18px;height:18px;background:var(--accent)}
.brand-name{font-family:"Tinos",serif;font-size:34px;color:var(--white)}
.account{position:absolute;top:0;left:904px;display:flex;height:37px}
.account a{display:flex;align-items:center;justify-content:center;font-family:"Oswald",sans-serif;
  font-size:17px;color:var(--white);text-decoration:none}
.login{width:82px;background:#2b2b2b}
.signup{width:81px;background:var(--accent)}
.search{position:absolute;left:700px;top:70px;width:367px;height:30px;background:#f2f2f2;
  border:1px solid #bbb;font-family:"Arimo",sans-serif;font-size:12px;color:#777;padding:7px 5px}
.search svg{position:absolute;right:7px;top:9px}
.main-nav{position:absolute;left:0;top:166px;width:1195px;height:86px;background:var(--nav-bg);
  border-bottom:4px solid var(--accent);height:90px}
.main-nav ul{list-style:none;display:flex;position:absolute;left:127px;top:0}
.main-nav li{width:157px;height:86px;border-right:1px solid var(--nav-line);color:var(--white);
  font-size:15px;text-align:center;padding-top:34px;position:relative}
.main-nav li.active{background:var(--accent);border-right:none}
.main-nav .caret{position:absolute;left:72px;top:55px}
.hero{position:absolute;left:0;top:256px;width:1195px;height:520px;
  background:linear-gradient(90deg,#6f8fb0 0%,#8ea4b4 30%,#d8d2c6 55%,#9a8f82 75%,#5a4030 100%)}
.hero-deck{position:absolute;left:0;bottom:0;width:100%;height:150px;
  background:linear-gradient(180deg,rgba(120,80,55,0) 0%,rgba(120,80,55,.7) 100%)}
.arrow{position:absolute;top:244px;width:33px;height:33px;background:#2a2a2a;display:flex;align-items:center;justify-content:center}
.arrow.prev{left:0}.arrow.next{right:0}
.caption{position:absolute;left:127px;top:186px;width:288px;height:228px;background:rgba(60,60,60,.88);
  padding:28px 17px;color:var(--white)}
.caption h2{font-weight:400;font-size:20px;line-height:24px}
.caption .sub{font-size:11px;line-height:14px}
.caption p{font-family:"Arimo",sans-serif;font-size:14px;line-height:22px;color:#ddd;margin-top:14px}
.caption a{display:inline-block;margin-top:14px;background:var(--accent);color:var(--white);
  font-family:"Arimo",sans-serif;font-size:13px;padding:11px 10px;text-decoration:none}
.featured{position:absolute;left:127px;top:822px;width:940px}
.featured h2{font-weight:400;font-size:35px;color:var(--title-grey);letter-spacing:-1.5px;
  border-bottom:1px solid var(--rule);padding-bottom:4px;height:47px}
.proposals{display:flex;margin-top:28px}
.proposal{width:240px;height:320px;border-left:1px solid var(--rule);padding-left:19px}
.proposal:first-child{border-left:none;padding-left:0}
.proposal h3{font-weight:400;font-size:27px;color:var(--heading);margin-top:8px}
.proposal .photo{width:200px;height:240px;margin-top:26px}
.p1{background:linear-gradient(180deg,#7aa6d8 0%,#8a4a33 35%,#6e5040 60%,#5f9a3a 100%)}
.p2{background:linear-gradient(180deg,#8fb2d4 0%,#d4d0c8 30%,#c8c4bc 80%,#6b8f6a 100%)}
.p3{background:linear-gradient(180deg,#7aa6da 0%,#c4d6ea 50%,#d8d6cc 70%,#5fa4a0 100%)}
.p4{background:linear-gradient(180deg,#2f5ea8 0%,#d6d6d6 35%,#cfcfcf 70%,#6fa040 100%)}
</style>
</head>
<body>
<header class="site-header">
  <div class="brand"><span class="brand-mark"></span><span class="brand-name">Hearth Lets</span></div>
  <nav class="account"><a class="login" href="#">LOGIN</a><a class="signup" href="#">SIGN UP</a></nav>
  <div class="search">Site Search
    <svg width="12" height="12" viewBox="0 0 12 12"><circle cx="4.5" cy="4.5" r="3.3" fill="none" stroke="#222" stroke-width="1.4"/><line x1="7" y1="7" x2="11" y2="11" stroke="#222" stroke-width="1.8"/></svg>
  </div>
</header>
<nav class="main-nav">
  <ul>
    <li class="active">MAIN</li>
    <li>ABOUT US<svg class="caret" width="12" height="7" viewBox="0 0 12 7"><polyline points="1,1 6,6 11,1" fill="none" stroke="#fff"/></svg></li>
    <li>SERVICES</li>
    <li>GALLERY<svg class="caret" width="12" height="7" viewBox="0 0 12 7"><polyline points="1,1 6,6 11,1" fill="none" stroke="#fff"/></svg></li>
    <li>BLOG</li>
    <li>CONTACTS</li>
  </ul>
</nav>
<section class="hero" role="img" aria-label="Modern house with glass doors opening onto a wooden terrace above a lake and mountains">
  <div class="hero-deck"></div>
  <span class="arrow prev"><svg width="12" height="14" viewBox="0 0 12 14"><polygon points="11,0 11,14 2,7" fill="#fff"/></svg></span>
  <span class="arrow next"><svg width="12" height="14" viewBox="0 0 12 14"><polygon points="1,0 1,14 10,7" fill="#fff"/></svg></span>
  <div class="caption">
    <h2>PROJECT NAME:</h2>
    <div class="sub">INTEGER ULLAMCORPER VIVERRA NIBH.</div>
    <p>Fusce in dolor eget dui bibendum eleifend id eu sem. Donec tempus diam eu quam.</p>
    <a href="#">MORE INFO</a>
  </div>
</section>
<section class="featured">
  <h2>FEATURED PROPOSALS</h2>
  <div class="proposals">
    <article class="proposal"><h3>Luxury Property</h3><div class="photo p1" role="img" aria-label="Brick house with cantilevered upper floor over a lawn"></div></article>
    <article class="proposal"><h3>Buying Home</h3><div class="photo p2" role="img" aria-label="Angular concrete house against a blue sky"></div></article>
    <article class="proposal"><h3>Selling Home</h3><div class="photo p3" role="img" aria-label="Modern villa with swimming pool under a wispy sky"></div></article>
    <article class="proposal"><h3>Renting</h3><div class="photo p4" role="img" aria-label="White modern house on a green slope"></div></article>
  </div>
</section>
</body>
</html>
```